Business card for a shipping supplies business

Needing a business card design. Please see the logo. The logo with the white font should be used if there is a dark background.

We are looking for the following info on the card. Please see the sample info. We will need the info to be changed with a few different employee names and info but all will use the same template.

Business Name: The Crate Heron
Employee Name : Derek Malloy
Position: Account Manager
Address: 4827 W. Ridge 918 S.
Fort Worth, TX 72348
email: Derek@thecrateheron.com
telephone: 866-417-2902 x 217
website: www.getcartonry.com

Target Market(s)

Businesses who ship products for online sales

Industry/Entity Type

Cardboard

Contact Information for Business Card

Name, title, address, website, logo, telephone number

Font styles to use
Sans Serif

Colors
EE7325
F08F49
F5BC92
FAE3D3
FDF4ED

Requirements
Must have
• Logo on back of card. Clean look, just logo, website address

```html
<!DOCTYPE html>
<html lang="en">
<head>
<meta charset="utf-8">
<title>The Crate Heron – Business Card</title>
<link href="https://fonts.googleapis.com/css2?family=Arimo:wght@400;700&display=swap" rel="stylesheet">
<style>
  :root {
    --orange: #e2591f;
    --orange-soft: #ee7325;
    --ink: #141414;
    --paper: #fbfbfa;
    --card-dark: #060709;
    --stage: #2a2b2e;
    --white: #ffffff;
  }
  * { box-sizing: border-box; margin: 0; padding: 0; }
  html, body { width: 1200px; height: 963px; overflow: hidden; }
  body {
    background: var(--stage);
    font-family: "Arimo", Arial, sans-serif;
    display: flex; flex-direction: column; align-items: center; justify-content: center;
    gap: 50px;
  }
  .card {
    width: 700px; height: 400px; position: relative; overflow: hidden;
    box-shadow: 0 10px 30px rgba(0,0,0,.45);
  }

  /* Front */
  .card-front { background: var(--paper); color: var(--ink); }
  .front-brand {
    position: absolute; left: 60px; top: 112px;
    display: flex; align-items: center; gap: 12px;
  }
  .brand-square { width: 22px; height: 22px; background: var(--orange); flex: none; }
  .brand-name { font-weight: 700; font-size: 32px; letter-spacing: .3px; color: var(--ink); white-space: nowrap; }
  .divider-dark {
    position: absolute; left: 60px; top: 178px; width: 310px; height: 2px; background: var(--ink);
  }
  .divider-orange {
    position: absolute; left: 370px; top: 178px; width: 280px; height: 2px; background: var(--orange-soft);
  }
  .contact-list {
    position: absolute; left: 60px; top: 198px; list-style: none;
    font-size: 17px; line-height: 30px;
  }
  .contact-list li { display: flex; align-items: center; gap: 10px; white-space: nowrap; }
  .contact-icon {
    width: 18px; height: 18px; border-radius: 4px; background: var(--orange);
    display: inline-flex; align-items: center; justify-content: center; flex: none;
  }
  .staff {
    position: absolute; right: 60px; top: 108px; text-align: right;
  }
  .staff-name { color: var(--orange); font-weight: 700; font-size: 22px; letter-spacing: .5px; text-transform: uppercase; white-space: nowrap; }
  .staff-title { font-size: 16px; margin-top: 4px; }
  .edge-tab {
    position: absolute; right: 0; top: 150px; width: 22px; height: 36px;
    background: var(--orange); border-radius: 6px 0 0 6px;
  }
  .address {
    position: absolute; right: 50px; top: 196px; text-align: right;
    font-size: 17px; line-height: 26px; font-style: normal;
  }

  /* Back */
  .card-back {
    background: var(--card-dark);
    display: flex; flex-direction: column; align-items: center; justify-content: center;
    gap: 22px;
  }
  .back-brand { display: flex; align-items: center; gap: 16px; }
  .back-brand .brand-square { width: 30px; height: 30px; }
  .back-brand .brand-name { color: var(--white); font-size: 46px; }
  .back-website { color: var(--orange-soft); font-size: 18px; letter-spacing: .5px; }
</style>
</head>
<body>

  <section class="card card-front" aria-label="Card front">
    <div class="front-brand">
      <span class="brand-square"></span>
      <span class="brand-name">The Crate Heron</span>
    </div>

    <div class="staff">
      <p class="staff-name">Derek Malloy</p>
      <p class="staff-title">Account Manager</p>
    </div>
    <span class="edge-tab"></span>

    <span class="divider-dark"></span>
    <span class="divider-orange"></span>

    <ul class="contact-list">
      <li>
        <span class="contact-icon">
          <svg width="12" height="12" viewBox="0 0 24 24"><path fill="#fff" d="M6.6 10.8a15 15 0 0 0 6.6 6.6l2.2-2.2c.3-.3.7-.4 1-.2 1.1.4 2.3.6 3.6.6.6 0 1 .4 1 1V20c0 .6-.4 1-1 1A17 17 0 0 1 3 4c0-.6.4-1 1-1h3.5c.6 0 1 .4 1 1 0 1.3.2 2.5.6 3.6.1.3 0 .7-.2 1z"/></svg>
        </span>
        866-417-2902 x 217
      </li>
      <li>
        <span class="contact-icon">
          <svg width="12" height="12" viewBox="0 0 24 24"><rect x="2" y="5" width="20" height="14" fill="none" stroke="#fff" stroke-width="2.4"/><path d="M2 6l10 7 10-7" fill="none" stroke="#fff" stroke-width="2.4"/></svg>
        </span>
        Derek@thecrateheron.com
      </li>
      <li>
        <span class="contact-icon">
          <svg width="12" height="12" viewBox="0 0 24 24"><circle cx="12" cy="12" r="9" fill="none" stroke="#fff" stroke-width="2.2"/><path d="M3 12h18M12 3c3 3 3 15 0 18M12 3c-3 3-3 15 0 18" fill="none" stroke="#fff" stroke-width="1.8"/></svg>
        </span>
        www.getcartonry.com
      </li>
    </ul>

    <address class="address">
      4827 W. Ridge 918 S.<br>
      Fort Worth, TX 72348
    </address>
  </section>

  <section class="card card-back" aria-label="Card back">
    <div class="back-brand">
      <span class="brand-square"></span>
      <span class="brand-name">The Crate Heron</span>
    </div>
    <p class="back-website">www.getcartonry.com</p>
  </section>

</body>
</html>
```